Company Letter head for real estate company

need company letter head
Updates

You can use the logo that I submitted. no need to create a new one

Requirements
Must have
• must have my address on it..38264 WINDMERE, CANTON, MI 48302-1175, INFO@MUVRO.CA

```html
<!DOCTYPE html>
<html lang="en">
<head>
<meta charset="utf-8">
<title>Northvale Letterhead</title>
<link rel="stylesheet" href="https://fonts.googleapis.com/css2?family=Encode+Sans+Semi+Condensed:wght@300;400&family=Lato:wght@400&family=Montserrat:wght@400;700&display=swap">
<style>
  :root {
    --backdrop: #e4e4e4;
    --paper: #ffffff;
    --ink: #555555;
    --ink-soft: #666666;
    --accent: #7fbf3a;
    --accent-faint: #eef5e6;
    --signature: #d9d9d9;
  }
  * { margin: 0; padding: 0; box-sizing: border-box; }
  html, body { width: 1056px; height: 1200px; overflow: hidden; background: var(--backdrop); }
  .letterhead {
    position: absolute; left: 112px; top: 12px;
    width: 831px; height: 1176px;
    background: var(--paper); overflow: hidden;
    color: var(--ink);
  }
  .brand {
    position: absolute; left: 100px; top: 92px;
    display: flex; align-items: center; gap: 12px;
  }
  .brand-dot { width: 22px; height: 22px; border-radius: 50%; background: var(--accent); }
  .brand-name {
    font-family: "Montserrat", sans-serif; font-weight: 700;
    font-size: 34px; letter-spacing: 3px; color: var(--ink);
  }
  .contact {
    position: absolute; left: 580px; top: 66px;
    font-family: "Lato", sans-serif; font-size: 15px; line-height: 19px; color: var(--ink-soft);
  }
  .contact .address { margin-bottom: 8px; }
  .contact ul { list-style: none; }
  .contact li { display: flex; align-items: center; gap: 12px; height: 21px; }
  .contact svg { width: 15px; height: 15px; flex: none; }
  .date {
    position: absolute; left: 100px; top: 340px;
    font-family: "Montserrat", sans-serif; font-size: 17px; color: var(--ink-soft);
  }
  .recipient-name {
    position: absolute; left: 100px; top: 372px;
    font-family: "Montserrat", sans-serif; font-weight: 700; font-size: 28px; color: var(--ink);
  }
  .recipient-title {
    position: absolute; left: 100px; top: 416px;
    font-family: "Montserrat", sans-serif; font-size: 17px; color: var(--ink-soft);
  }
  .body-copy {
    position: absolute; left: 100px; top: 484px; width: 631px;
    font-family: "Encode Sans Semi Condensed", sans-serif; font-weight: 300;
    font-size: 14px; line-height: 21px; text-align: justify; color: var(--ink);
  }
  .body-copy p + p { margin-top: 21px; }
  .closing {
    position: absolute; left: 100px; top: 804px;
    font-family: "Encode Sans Semi Condensed", sans-serif; font-weight: 400; font-size: 17px;
  }
  .signature {
    position: absolute; left: 100px; top: 860px; width: 90px; height: 44px;
    background: var(--signature); border-radius: 4px;
  }
  .footer-band {
    position: absolute; left: 0; bottom: 0; width: 100%; height: 210px;
    background: linear-gradient(to bottom, rgba(238,245,230,0) 0%, var(--accent-faint) 100%);
  }
  .footer-name {
    position: absolute; left: 0; bottom: 40px; width: 100%; text-align: center;
    font-family: "Montserrat", sans-serif; font-weight: 700; font-size: 96px;
    letter-spacing: 10px; color: var(--accent-faint);
  }
</style>
</head>
<body>
<main class="letterhead">
  <header>
    <div class="brand">
      <span class="brand-dot"></span>
      <span class="brand-name">NORTHVALE</span>
    </div>
    <address class="contact">
      <div class="address">1234 First Line Address<br>5678 Second Line Address</div>
      <ul>
        <li><svg viewBox="0 0 24 24"><path fill="var(--accent)" d="M6.6 10.8a15 15 0 0 0 6.6 6.6l2.2-2.2c.3-.3.7-.4 1-.2 1.1.4 2.3.6 3.6.6.6 0 1 .4 1 1V20c0 .6-.4 1-1 1A17 17 0 0 1 3 4c0-.6.4-1 1-1h3.5c.6 0 1 .4 1 1 0 1.3.2 2.5.6 3.6.1.3 0 .7-.2 1z"/></svg>(777) 888-7777</li>
        <li><svg viewBox="0 0 24 24"><rect x="2" y="5" width="20" height="14" fill="var(--accent)"/><path d="M2 5l10 8 10-8" fill="none" stroke="#fff" stroke-width="1.6"/></svg>info@yourmail.com</li>
        <li><svg viewBox="0 0 24 24"><circle cx="12" cy="12" r="9" fill="none" stroke="var(--accent)" stroke-width="2"/><path d="M3 12h18M12 3c3 3 3 15 0 18M12 3c-3 3-3 15 0 18" fill="none" stroke="var(--accent)" stroke-width="1.5"/></svg>www.yourwebsite.com</li>
      </ul>
    </address>
  </header>

  <p class="date">01 December, 2021</p>
  <h1 class="recipient-name">DANIEL CARTER</h1>
  <p class="recipient-title">Cheif Executive Officer</p>

  <section class="body-copy">
    <p>Contrary to popular belief, Lorem Ipsum is not simply random text. It has roots in a piece of classical Latin literature from 45 BC, making it over 2000 years old. Harold Whitcombe, a Latin professor at Larkspur College in Virginia, looked up one of the more obscure Latin words, consectetur. The standard chunk of Lorem Ipsum used since the 1500s is reproduced below for those interested.</p>
    <p>Lorem Ipsum comes from sections 1.10.32 and 1.10.33 of "de Finibus Bonorum et Malorum" (The Extremes of Good and Evil) by Quintus Aurel, written in 45 BC. This book is a treatise on the theory of ethics, very popular during the Renaissance. The first line of Lorem Ipsum.This book is a treatise on the theory of ethics, very popular during the Renaissance. The first line of Lorem Ipsum.</p>
    <p>The standard chunk of Lorem Ipsum used since the 1500s is reproduced below for those interested. This book is a treatise on the theory of ethics, very popular during the Renaissance. The first line of Lorem Ipsum. The first line of Lorem Ipsum.This book is a treatise on the theory of ethics, very popular during the Renaissance.</p>
  </section>

  <p class="closing">Best Regards</p>
  <div class="signature" role="img" aria-label="Handwritten signature of the sender"></div>

  <footer>
    <div class="footer-band"></div>
    <div class="footer-name">NORTHVALE</div>
  </footer>
</main>
</body>
</html>
```